Talvor GmbH business card

We Talvor GmbH based in Switzerland are looking for a business card design. The Fresh Jung, appealing to customers of all kinds. We already have a logo to upload but still a business card. Details: Talvor GmbH Address: Lindenweg 14b in 9476 Brugwil. Tel: 41 79 462 37 18, web: Talvor.ch, E-mail: info@Talvor.ch Facebook: Talvor GmbH. I am the Managing Director: Luka Petrovac. On reverse: Title: Transporter and bus rental Gross: Without deposit Super prices
Contact Information for Business Card
Siehe Projektbeschreibung
Requirements
Should not have
- Other pictures

```html
<!DOCTYPE html>
<html lang="de">
<head>
<meta charset="utf-8">
<title>Talvor GmbH – Visitenkarte</title>
<link rel="stylesheet" href="https://fonts.googleapis.com/css2?family=Barlow+Semi+Condensed:wght@600&family=Open+Sans:wght@400;600&display=swap">
<style>
  :root {
    --navy: #000a6e;
    --steel: #7f9bb5;
    --ink-grey: #555558;
    --paper: #ffffff;
    --backdrop: #ebebee;
  }
  * { box-sizing: border-box; margin: 0; padding: 0; }
  html, body {
    width: 1105px;
    height: 1200px;
    overflow: hidden;
    background: var(--backdrop);
    font-family: "Open Sans", Arial, sans-serif;
  }
  .card {
    position: absolute;
    left: 192px;
    width: 720px;
    height: 412px;
    background: var(--paper);
    overflow: hidden;
  }
  .card--front { top: 150px; }
  .card--back { top: 640px; }

  .brand {
    position: absolute;
    left: 0; right: 0;
    display: flex;
    align-items: center;
    justify-content: center;
    gap: 14px;
    color: var(--navy);
    font-family: "Barlow Semi Condensed", Arial, sans-serif;
    font-weight: 600;
    letter-spacing: 1px;
  }
  .brand__mark {
    width: 30px;
    height: 30px;
    background: var(--navy);
  }
  .card--front .brand { top: 80px; font-size: 60px; line-height: 72px; }

  .name-band {
    position: absolute;
    top: 226px;
    left: 0; right: 0;
    height: 78px;
    background: var(--steel);
    text-align: center;
    color: var(--navy);
  }
  .name-band__name {
    display: block;
    margin-top: 14px;
    font-family: "Barlow Semi Condensed", Arial, sans-serif;
    font-weight: 600;
    font-size: 25px;
    line-height: 28px;
    letter-spacing: 0.5px;
  }
  .name-band__role {
    display: block;
    font-size: 18px;
    line-height: 22px;
  }
  .contact-band {
    position: absolute;
    top: 307px;
    left: 0; right: 0;
    bottom: 0;
    background: var(--navy);
    color: var(--paper);
    text-align: center;
    font-size: 18px;
  }
  .contact-band__address {
    margin-top: 22px;
    line-height: 24px;
  }
  .contact-band__lines {
    margin-top: 6px;
    display: flex;
    justify-content: center;
    gap: 16px;
    line-height: 24px;
  }
  .contact-item { display: inline-flex; align-items: center; gap: 5px; }
  .contact-item svg { width: 17px; height: 17px; fill: var(--paper); }

  .card--back .brand { top: 130px; font-size: 96px; line-height: 110px; gap: 20px; }
  .card--back .brand__mark { width: 40px; height: 40px; }
  .offer {
    position: absolute;
    top: 308px;
    left: 0; right: 0;
    text-align: center;
    color: var(--ink-grey);
  }
  .offer__service { font-size: 19px; line-height: 26px; }
  .offer__claim { font-size: 31px; font-weight: 600; line-height: 42px; }
  .offer__price { font-size: 22px; font-weight: 400; }
</style>
</head>
<body>
  <section class="card card--front" aria-label="Vorderseite">
    <div class="brand"><span class="brand__mark"></span><span class="brand__name">Talvor GmbH</span></div>
    <div class="name-band">
      <span class="name-band__name">LUKA PETROVAC</span>
      <span class="name-band__role">Manager</span>
    </div>
    <div class="contact-band">
      <p class="contact-band__address">Lindenweg 14b in 9476 Brugwil.</p>
      <p class="contact-band__lines">
        <span class="contact-item">
          <svg viewBox="0 0 24 24" aria-hidden="true"><path d="M6.6 10.8a15.1 15.1 0 0 0 6.6 6.6l2.2-2.2a1 1 0 0 1 1-.25 11.4 11.4 0 0 0 3.6.57 1 1 0 0 1 1 1V20a1 1 0 0 1-1 1A17 17 0 0 1 3 4a1 1 0 0 1 1-1h3.5a1 1 0 0 1 1 1c0 1.25.2 2.45.57 3.57a1 1 0 0 1-.25 1z"/></svg>+41 79 462 37 18
        </span>
        <span class="contact-item">
          <svg viewBox="0 0 24 24" aria-hidden="true"><path d="M2 5h20v14H2z M3.5 6.5l8.5 6.5 8.5-6.5" fill="none" stroke="#fff" stroke-width="0"/><path d="M2 5h20v2l-10 7L2 7zM2 9l10 7 10-7v10H2z"/></svg>info@Talvor.ch
        </span>
        <span class="contact-item">
          <svg viewBox="0 0 24 24" aria-hidden="true"><circle cx="12" cy="12" r="10"/><path d="M2 12h20M12 2c3 3 3 17 0 20M12 2c-3 3-3 17 0 20" fill="none" stroke="#000a6e" stroke-width="1.6"/></svg>Talvor.ch
        </span>
      </p>
    </div>
  </section>

  <section class="card card--back" aria-label="Rückseite">
    <div class="brand"><span class="brand__mark"></span><span class="brand__name">Talvor</span></div>
    <div class="offer">
      <p class="offer__service">Transporter und Bus Vermietung</p>
      <p class="offer__claim">Ohne Kaution <span class="offer__price">Super Preise</span></p>
    </div>
  </section>
</body>
</html>
```